TARPLOAD business card design

TARPLOAD is a manufacturer of skip bags supplying both the domestic and commercial market. We wish to convey core characteristics of strength, professionalism and reliability to our customers. We are after a business card that uses our company colours of black and yellow as well as incorporating our logo. Our customers are predominantly in the construction or hardware industry. It is important the cards are professional as we are a small company wishing to appear larger than we actually are. more info on the company and product available at www.tarpload-example.com.au

Target Market(s)

hardware buyers, contruction company owners

Industry/Entity Type

Construction

Requirements
Must have
• company colours of black and yellow - No other colours or variation of yellow black. our company logo. card design must convey "tough"
• Card design must be landscape
• Details to be included on the card are:
• Name and Tiltle
• Phone number : 1300 41 62 53
• Mobile: 0452 718 903
• Fax: 03 9617 4852
• email: dale.hendry@tarpload-example.com.au
• address: PO Box 517, Kelvindale, VIC,3294
• Text in white when on a black background
Nice to have
• I like the idea of the back of the card being black with lighter circle area in the middle with black logo in the centre. Similar to the attached "iconic" card

```html
<!DOCTYPE html>
<html lang="en">
<head>
<meta charset="utf-8">
<title>TARPLOAD business card</title>
<link rel="stylesheet" href="https://fonts.googleapis.com/css2?family=Saira:wght@300;400;800&display=swap">
<style>
  :root {
    --black: #000000;
    --yellow: #f2cd00;
    --white: #ffffff;
    --stage: #ffffff;
    --glow: #2a2a2a;
  }
  * { margin: 0; padding: 0; box-sizing: border-box; }
  html, body {
    width: 1200px;
    height: 800px;
    overflow: hidden;
    background: var(--stage);
  }
  .canvas {
    position: relative;
    width: 1200px;
    height: 800px;
    font-family: "Saira", Arial, sans-serif;
  }
  .card {
    position: absolute;
    top: 195px;
    width: 554px;
    height: 316px;
    background: var(--black);
    overflow: hidden;
  }
  .card--front { left: 27px; }
  .card--back { left: 625px; }

  /* Front */
  .front-brand-panel {
    position: absolute;
    left: 366px;
    top: 0;
    width: 188px;
    height: 100%;
    background: var(--yellow);
  }
  .brand-name {
    position: absolute;
    left: 0;
    width: 100%;
    text-align: center;
    font-weight: 800;
    letter-spacing: 0.5px;
  }
  .front-brand-panel .brand-name {
    top: 240px;
    font-size: 29px;
    line-height: 1;
    color: var(--black);
  }
  .contact {
    position: absolute;
    left: 22px;
    top: 100px;
    color: var(--white);
  }
  .contact__name {
    font-weight: 800;
    font-size: 22px;
    line-height: 26px;
    letter-spacing: 0.6px;
    text-transform: uppercase;
  }
  .contact__title {
    font-weight: 300;
    font-size: 17.5px;
    line-height: 22px;
  }
  .contact__lines {
    list-style: none;
    font-weight: 300;
    font-size: 16.5px;
    line-height: 21px;
  }
  .contact__lines--phones { margin-top: 12px; }
  .contact__lines--address { margin-top: 12px; }
  .contact__label { display: inline-block; width: 15px; }

  /* Back */
  .back-glow {
    position: absolute;
    left: 60px;
    top: 70px;
    width: 434px;
    height: 190px;
    background: radial-gradient(ellipse at center, var(--glow) 0%, rgba(30,30,30,0.6) 40%, rgba(0,0,0,0) 72%);
  }
  .card--back .brand-name {
    top: 136px;
    font-size: 28px;
    line-height: 1;
    color: var(--yellow);
  }
  .back-url {
    position: absolute;
    left: 0;
    top: 196px;
    width: 100%;
    text-align: center;
    font-weight: 300;
    font-size: 17px;
    letter-spacing: 0.8px;
    color: var(--yellow);
  }
</style>
</head>
<body>
<main class="canvas">
  <section class="card card--front" aria-label="Card front">
    <div class="contact">
      <p class="contact__name">Dale Hendry</p>
      <p class="contact__title">Managing Director</p>
      <ul class="contact__lines contact__lines--phones">
        <li><span class="contact__label">P</span>1300.41.62.53</li>
        <li><span class="contact__label">M</span>0452.718.903</li>
        <li><span class="contact__label">F</span>03.9617.4852</li>
      </ul>
      <ul class="contact__lines contact__lines--address">
        <li>PO BOX 517</li>
        <li>Kelvindale, VIC, 3294</li>
        <li>dale.hendry@tarpload-example.com.au</li>
      </ul>
    </div>
    <div class="front-brand-panel">
      <p class="brand-name">TARPLOAD</p>
    </div>
  </section>

  <section class="card card--back" aria-label="Card back">
    <div class="back-glow" role="img" aria-label="Soft lit area with fine vertical line texture behind the company name"></div>
    <p class="brand-name">TARPLOAD</p>
    <p class="back-url">tarpload-example.com.au</p>
  </section>
</main>
</body>
</html>
```